Torvela Golf 2016 - national wide golf tournament

We organize a national golf tournament for the Young Merchants Fellowship Switzerland (see http://www.tmq-velor.ch for further information).
The tournament is every year but 2016 it is our goal to organize the best golf tournament ever in a very exclusive environment (Golfclub Ravenhollt, http://www.ravenhollt.ch/wp/). There will be about 80 golfers and 150 guests in the evening. The tournament 2015 uses this website: http://www.torvelagolf.ch.

We need a completely new web design to organize our event in 2016. The website should inform about all event details and enable a online self registration. We have a logo for the event and the colors should be reused. We would like to see designs with the logo colors. The main page should be a simple one page-layout with different layout blocks directly accessible via top sticky menubar:
- Home (welcome page)
- Program
- Information
- Registration (formular on homepage)
- Sponsors
- Contact

Important: On the welcome page there should be enough place for:
1. Our Golf event logo
2. Our Torvela Switzerland logo
3. The Golfclub logo
4. The main sponsors logos (see TRVS_Sponsors_Section.png and http://www2.torvela.ch as input, not necessary to design it the same way)

The website will be in German in the first place but we need it multilingual.

Please see attachment for logos and pictures.
The web site will be implemented on WordPress - this is not part of this PixelMarket project.

Target Market(s)

Torvela Members Switzerland, Golfers in Switzerland

Number of Pages Required

3 page

Font styles to use
Sans Serif

Colors
9bcb3c
abd037
cadf82
eaf2ce
f6faec
ffffff
ecf7fb
cee9f5
85cae6

Requirements
Must have
• - multilingual (DE / FR)
• - one page layout design for main site / welcome site
• - page layout for big picture less text
• - page layout for multiple smaller pictures and multiple text blocks
• - bright design including the colors of the Torvela Golf 2016 logo (greens)
• - space for pictures of the golf club / golf playeres / other
• - main sponsors logos on the front page
• - mobile version / responsive design
Nice to have
• - sponsor section => what idea do you have?
• - slider with picture on mainpage => as on tmq-velor.ch

```html
<!DOCTYPE html>
<html lang="en">
<head>
<meta charset="utf-8">
<title>Torvela Golf 2016</title>
<link href="https://fonts.googleapis.com/css2?family=Open+Sans:wght@400;600;700&family=Montserrat:wght@400;600&display=swap" rel="stylesheet">
<style>
:root{
  --green:#6e9a2f;
  --green-dark:#3f5f2a;
  --band-mid:#6f9a34;
  --band-edge:#4c7326;
  --footer:#2f5128;
  --ink:#222;
  --text:#444;
  --muted:#777;
  --sponsor:#555;
  --soft-bg:#f5f5f5;
  --line:#9a9a9a;
  --white:#fff;
}
*{box-sizing:border-box;margin:0;padding:0}
html,body{width:1200px;height:2786px;overflow:hidden;background:var(--white)}
body{position:relative;font-family:"Open Sans",Arial,sans-serif;color:var(--text)}
.section-title{position:absolute;left:0;width:1200px;text-align:center;font-size:24px;font-weight:700;color:var(--ink);letter-spacing:.5px}

/* header */
.site-header{position:absolute;left:0;top:0;width:1200px;height:178px;background:var(--white)}
.brand{position:absolute;left:100px;top:40px;display:flex;align-items:center;gap:10px}
.brand-mark{width:44px;height:44px;border-radius:50%;background:var(--green)}
.brand-name{font-size:22px;font-weight:600;color:var(--green-dark);line-height:1.2;width:140px}
.lang{position:absolute;left:784px;top:37px;width:151px;height:41px;border:1px solid #ddd;font-size:11px;color:#555;display:flex;align-items:center;padding-left:16px;gap:14px}
.btn-online{position:absolute;left:948px;top:37px;width:152px;height:41px;background:var(--green);color:var(--white);font-size:13px;display:flex;align-items:center;justify-content:center}
.main-nav{position:absolute;left:552px;top:125px;display:flex;font-size:14px;font-weight:600;color:#222}
.main-nav a{display:block;height:31px;line-height:31px;padding:0 14px;color:inherit;text-decoration:none}
.main-nav a.active{background:var(--green);color:var(--white);width:80px;text-align:center;margin-right:6px}

/* hero */
.hero{position:absolute;left:0;top:178px;width:1200px;height:538px}
.hero-photo{position:absolute;inset:0;background:linear-gradient(180deg,#b9cde0 0%,#d8e2ea 30%,#7f9a52 48%,#6f963c 62%,#5d8a3a 80%,#7fa24a 100%)}
.hero-arrow{position:absolute;top:233px;width:38px;height:38px;border-radius:50%;background:rgba(80,80,80,.55)}
.hero-caption{position:absolute;left:247px;top:426px;width:702px;height:69px;background:rgba(255,255,255,.72);font-size:15px;color:#333;text-align:center;padding:10px 30px;line-height:1.6}

/* program */
.program-col{position:absolute;top:828px}
.program-col h3{font-size:18px;font-weight:600;color:var(--ink);margin-bottom:18px}
.program-col p{font-size:12px;line-height:17px;color:#333;margin-bottom:12px}
.thumb{position:absolute;top:1074px;width:231px;height:149px}
.dots{position:absolute;top:1251px;left:576px;display:flex;gap:6px}
.dots span{width:7px;height:7px;border-radius:50%;background:#ccc}
.dots span.on{background:var(--green)}

/* information */
.info{position:absolute;left:0;top:1304px;width:1200px;height:285px;background:var(--soft-bg)}
.info-text{position:absolute;left:100px;top:93px;width:1000px;font-size:11.5px;line-height:18px;color:var(--muted);text-align:center}
.partner-name{position:absolute;left:394px;top:202px;font-size:20px;font-weight:700;color:#2a6fb3}
.partner-badge{position:absolute;left:790px;top:196px;width:40px;height:50px;background:#d3a83a}

/* registrations */
.register{position:absolute;left:0;top:1590px;width:1200px;height:210px;background:radial-gradient(ellipse at center,var(--band-mid) 40%,var(--band-edge) 100%)}
.register h2{position:absolute;left:115px;top:58px;font-size:28px;font-weight:700;color:var(--white);letter-spacing:.5px}
.register p{position:absolute;left:115px;top:102px;width:680px;font-size:12.5px;line-height:17px;color:var(--white)}
.btn-register{position:absolute;left:838px;top:78px;width:264px;height:56px;background:var(--green-dark);color:var(--white);font-size:20px;display:flex;align-items:center;justify-content:center}

/* sponsors */
.sponsor-row{position:absolute;left:98px;top:1925px;width:1004px;display:flex;justify-content:space-between;align-items:center}
.sponsor{font-size:17px;font-weight:700;color:var(--sponsor)}
.sponsor-arrow{position:absolute;top:1928px;font-size:20px;color:#666}

/* contact */
.contact{position:absolute;left:0;top:2062px;width:1200px;height:547px;background:var(--soft-bg)}
.contact-item{position:absolute;top:113px;width:300px;text-align:center;font-family:"Montserrat",Arial,sans-serif;font-size:11.5px;line-height:22px;color:var(--muted);letter-spacing:1px}
.contact-item svg{display:block;margin:0 auto 12px}
.field{position:absolute;border:1px solid var(--line);font-family:"Montserrat",Arial,sans-serif;font-size:11px;color:#777;letter-spacing:1px;padding:12px 18px}
.btn-submit{position:absolute;left:957px;top:454px;width:145px;height:43px;background:var(--green);color:var(--white);font-family:"Montserrat",Arial,sans-serif;font-size:11px;font-weight:600;letter-spacing:1px;display:flex;align-items:center;justify-content:center}

/* footer */
.site-footer{position:absolute;left:0;top:2609px;width:1200px;height:177px;background:var(--footer);color:var(--white);text-align:center}
.social{position:absolute;top:62px;left:0;width:1200px;display:flex;justify-content:center;gap:22px;font-size:11px;font-weight:600}
.copyright{position:absolute;top:117px;left:0;width:1200px;font-family:"Montserrat",Arial,sans-serif;font-size:11px;letter-spacing:.5px}
</style>
</head>
<body>

<header class="site-header">
  <div class="brand"><span class="brand-mark"></span><span class="brand-name">Torvela Golf 2016</span></div>
  <div class="lang"><span>Language:</span><span>EN</span>
    <svg width="10" height="6" viewBox="0 0 10 6"><path d="M1 1l4 4 4-4" fill="none" stroke="#777" stroke-width="1.3"/></svg>
  </div>
  <div class="btn-online">Online Registration</div>
  <nav class="main-nav">
    <a class="active">Home</a><a>Program</a><a>Information</a><a>Registration</a><a>Sponsors</a><a>Contact</a>
  </nav>
</header>

<section class="hero">
  <div class="hero-photo" role="img" aria-label="Golf course with a green fairway, water hazard and trees under a bright sky"></div>
  <svg class="hero-arrow" style="left:36px" viewBox="0 0 38 38"><path d="M23 11l-9 8 9 8z" fill="#fff"/></svg>
  <svg class="hero-arrow" style="left:1124px" viewBox="0 0 38 38"><path d="M15 11l9 8-9 8z" fill="#fff"/></svg>
  <div class="hero-caption">Lorem ipsum dolor sit amet, consectetur adipiscing elit. Nunc quis diam lobortis, varius turpis a, tincidunt ligula. Aenean malesuada</div>
</section>

<section class="program">
  <h2 class="section-title" style="top:747px">PROGRAM</h2>
  <div class="program-col" style="left:98px;width:295px">
    <h3>Freitag</h3>
    <p>Anreise und gemütlicher Einstieg.<br>18.00 Uhr Zonensitzung im Hotel Castor Alp.<br>18.00 Uhr Kandidatenseminar Hotel Castor Alp.<br>Nachtessen im Hotel Castor Alp (fakultativ)</p>
  </div>
  <div class="program-col" style="left:407px;width:330px">
    <h3>Samstag</h3>
    <p>Ab 8.00 Uhr Torvela Golfmeisterschaften auf dem Parcours des Alpenfalke Cups auf über 2800 Meter.</p>
    <p>Ab 10.00 Uhr Partnerprogramm sportlich oder gemütlich rund um den Gornergrat.</p>
    <p>Abendprogramm:</p>
    <p>Ort: Hotel Lindengrat, Restaurant Albrecht, Zermatt</p>
  </div>
  <div class="program-col" style="left:782px;width:320px">
    <h3>Ablauf:</h3>
    <p>19.00 Uhr Treffpunkt zum Apéro, Begrüssung durch Organisatoren</p>
    <p>19.30 Uhr Rangverkündigung</p>
    <p>20.00 Uhr Nachtessen</p>
    <p>22.00 Uhr Ausklang</p>
  </div>
  <div class="thumb" style="left:98px;background:linear-gradient(135deg,#a26a34,#5a3418)" role="img" aria-label="Warmly lit hotel wine cellar interior"></div>
  <div class="thumb" style="left:355px;background:linear-gradient(180deg,#8fb0d8,#c9a46c 50%,#6d7e4a)" role="img" aria-label="Village street with historic houses and flowers"></div>
  <div class="thumb" style="left:611px;background:linear-gradient(180deg,#3f7fd0,#e8e8e8 55%,#7a8a6a)" role="img" aria-label="Alpine hotel building with a white tent in front"></div>
  <div class="thumb" style="left:869px;background:linear-gradient(180deg,#c8d4e0,#dedede 50%,#8a8a86)" role="img" aria-label="Chalet style hotel with an event tent"></div>
  <div class="dots"><span class="on"></span><span></span><span></span><span></span></div>
</section>

<section class="info">
  <h2 class="section-title" style="top:42px">INFORMATION</h2>
  <p class="info-text">Nulla risus orci, rutrum ac vestibulum ut, rhoncus ut dui. Etiam dapibus diam id accumsan vulputate. Nulla vel condimentum tortor. Suspendisse vulputate turpis nec quam feugiat, in porta nunc rhoncus. Class aptent taciti sociosqu ad litora torquent per conubia nostra, per inceptos himenaeos. Praesent ornare sollicitudin lacus, id condimentum sem convallis eget. Cras eleifend erat eget arcu accumsan euismod in et mi. Donec ut neque sed nibh cursus dignissim eget id neque. Etiam a feugiat erat. In hendrerit augue in velit pharetra, et commodo nunc placerat. Vivamus ut neque mattis mauris</p>
  <div class="partner-name">Young Merchants Fellowship Bern</div>
  <div class="partner-badge"></div>
</section>

<section class="register">
  <h2>REGISTRATIONS</h2>
  <p>Lorem ipsum dolor sit amet, consectetur adipiscing elit. Nunc quis diam lobortis, varius turpis a, tincidunt ligula. Aenean malesuada diam et justo faucibus porta in ac ipsum. Morbi sit amet lectus vestibulum, consectetur dui non, luctus dui. Quisque et ligula condimentum, elementum nisl a, tempus tellus.</p>
  <div class="btn-register">Register Now</div>
</section>

<section class="sponsors">
  <h2 class="section-title" style="top:1835px">SPONSORS</h2>
  <span class="sponsor-arrow" style="left:60px">‹</span>
  <div class="sponsor-row">
    <span class="sponsor">Velsano</span>
    <span class="sponsor">Marvo</span>
    <span class="sponsor">Kestrel Assur</span>
    <span class="sponsor">Brunnfeld Akademie</span>
    <span class="sponsor">Nordkamm Textil</span>
    <span class="sponsor">Bergholz</span>
  </div>
  <span class="sponsor-arrow" style="left:1131px">›</span>
</section>

<section class="contact">
  <h2 class="section-title" style="top:42px">CONTACT US</h2>
  <div class="contact-item" style="left:106px">
    <svg width="22" height="20" viewBox="0 0 22 20"><rect x="1" y="1" width="20" height="13" fill="none" stroke="#111" stroke-width="2"/><rect x="8" y="15" width="6" height="2" fill="#111"/><rect x="5" y="17" width="12" height="2" fill="#111"/></svg>
    info@torvelagolf.ch
  </div>
  <div class="contact-item" style="left:450px">
    <svg width="22" height="20" viewBox="0 0 22 20"><path d="M11 1L1 10h3v9h5v-6h4v6h5v-9h3z" fill="#111"/></svg>
    Torvela Brig, Livia Sarnach<br>Wiesengrundstr. 14<br>3901 Talheim
  </div>
  <div class="contact-item" style="left:792px">
    <svg width="20" height="20" viewBox="0 0 20 20"><path d="M4 1l4 4-2 3c1 3 3 5 6 6l3-2 4 4-3 3C8 19 1 12 1 4z" fill="#111"/></svg>
    079 000 12 34
  </div>
  <div class="field" style="left:98px;top:246px;width:491px;height:43px">Subject*</div>
  <div class="field" style="left:98px;top:312px;width:491px;height:43px">Name*</div>
  <div class="field" style="left:98px;top:379px;width:491px;height:43px">Email*</div>
  <div class="field" style="left:613px;top:246px;width:489px;height:176px">Message</div>
  <div class="btn-submit">SUBMIT</div>
</section>

<footer class="site-footer">
  <div class="social"><span>Linko</span><span>Chirp</span><span>Dotto</span><span>Plux</span><span>Vidz</span></div>
  <div class="copyright">© 2015 - yoursite All Right Reserved</div>
</footer>

</body>
</html>
```